Waterless soap seeking funky new design

We are looking for a talented designer to create a fresh and appealing label design for one of our current products. We do have a current logo that we really like and use in several places. We would like the new label design to work with and incorporate the current logo.
The product is our Gravel Tide wipe-off soap. It is made by hand, in small batches. We would like the label design to reflect the hand made aspect of the product. We are not requiring the label to be illustrated but we do like the hand drawn and hand made tie. and the illustration does appeal to us.
Please see the attached current logo that we do like. you can see it used in the attached current label, that we DONT like. this is what we are seeking, a new label for our Gravel Tide soap.
The soap is made for real messes, grease, grime and busted knuckles. It is made using natural ingredients. this is not a Men Only product, it is definitely geared toward men and would like the label to reflect that.

Target Market(s)

Mechanics, tradesmen, welders, People who get dirty for a living

Colors
0054AA
0677BA
7BADD7
CADEEF
E8F1F8
EE7325
F08F49
F5BC92
FAE3D3
FDF4ED
EB3D1F
EC4F4E
F09395
F8D3D4
FCEDEE

Requirements
Must have
• Keep the current logo. It can play a smaller role in the label, but we do use this logo else were in other promo items, and we don't want it to be completely gone.
Nice to have
• I would like to have something illustrated, I am not sold on this but I like the idea of a hand drawn(or at least in part) label to tie into the 'hand made' aspect
Should not have
• Current Font styles, We are currently selling product but we don't care for our font styles.

```html
<!DOCTYPE html>
<html lang="en">
<head>
<meta charset="utf-8">
<title>Gravel Tide Wipe-Off Soap Label</title>
<link rel="stylesheet" href="https://fonts.googleapis.com/css2?family=Montserrat:wght@600;700;800&display=swap">
<style>
  :root {
    --navy: #0a3d70;
    --gold: #e0a526;
    --red: #e8401c;
    --orange: #f5a623;
    --leaf-orange: rgba(232, 72, 30, 0.55);
    --leaf-gold: rgba(224, 165, 38, 0.5);
    --leaf-blue: rgba(123, 173, 215, 0.22);
    --white: #ffffff;
    --page: #f4f4f4;
  }
  html, body {
    margin: 0;
    padding: 0;
    width: 844px;
    height: 1200px;
    overflow: hidden;
    background: var(--page);
    font-family: "Montserrat", Arial, sans-serif;
  }
  .label {
    position: absolute;
    left: 42px;
    top: 278px;
    width: 760px;
    height: 643px;
    background: var(--navy);
    overflow: hidden;
  }
  .label__foliage {
    position: absolute;
    inset: 0;
    background:
      radial-gradient(ellipse 150px 240px at 60px 300px, var(--leaf-orange), transparent 70%),
      radial-gradient(ellipse 150px 260px at 700px 300px, var(--leaf-orange), transparent 70%),
      radial-gradient(ellipse 220px 110px at 330px 40px, var(--leaf-gold), transparent 70%),
      radial-gradient(ellipse 230px 100px at 390px 620px, var(--leaf-gold), transparent 70%),
      radial-gradient(ellipse 260px 200px at 130px 90px, var(--leaf-blue), transparent 70%),
      radial-gradient(ellipse 260px 200px at 640px 560px, var(--leaf-blue), transparent 70%),
      radial-gradient(ellipse 240px 180px at 130px 560px, var(--leaf-blue), transparent 70%),
      var(--navy);
  }
  .label__frame {
    position: absolute;
    inset: 10px;
    border: 2px solid var(--gold);
  }
  .panel {
    position: absolute;
    left: 166px;
    top: 141px;
    width: 409px;
    height: 349px;
    background: var(--white);
    border: 9px solid var(--red);
  }
  .panel > * {
    position: absolute;
    left: 0;
    right: 0;
    margin: 0;
    text-align: center;
    white-space: nowrap;
  }
  .brand {
    top: 44px;
    display: flex;
    justify-content: center;
    align-items: center;
    gap: 12px;
    color: var(--red);
    font-weight: 800;
    font-size: 20px;
  }
  .brand__dot {
    width: 60px;
    height: 60px;
    border-radius: 50%;
    background: var(--orange);
  }
  .claim {
    top: 143px;
    color: var(--red);
    font-weight: 700;
    font-size: 20px;
  }
  .natural {
    top: 178px;
    color: var(--navy);
    font-weight: 700;
    font-size: 16px;
    letter-spacing: 4px;
  }
  .product {
    top: 206px;
    color: var(--red);
    font-weight: 800;
    font-size: 46px;
    line-height: 1;
    letter-spacing: 1px;
  }
  .product-type {
    top: 260px;
    color: var(--navy);
    font-weight: 700;
    font-size: 34px;
    line-height: 1;
  }
  .tagline {
    top: 309px;
    color: var(--red);
    font-weight: 700;
    font-size: 12px;
  }
</style>
</head>
<body>
  <div class="label">
    <div class="label__foliage" role="img" aria-label="Hand-drawn leafy branches in orange, gold and soft blue outline across the navy field"></div>
    <div class="label__frame"></div>
    <div class="panel">
      <div class="brand"><span class="brand__dot"></span><span>Brass Otter Soap Co.</span></div>
      <p class="claim">Eczema Friendly</p>
      <p class="natural">All Natural Ingredients</p>
      <p class="product">GRAVEL TIDE</p>
      <p class="product-type">WIPE-OFF SOAP</p>
      <p class="tagline">No Water? No Problem.</p>
    </div>
  </div>
</body>
</html>
```